Book cover entitled #GLOWBEYONDIT

Design front book cover (self-self-portait photos included) for my first book entitled -

#GLOWBEYONDIT (may be best to have different shades of colour for glow beyond it to stand off you). I'm intentionally choosing a title that is essentially a hashtag.

Subtitle - Rewriting quiet inner battles

Concept of cover - left side of my face is shaded with shame and right side is brighter and hopeful. I have also include my logo.

Link for photos
https://www.filqorvex.com/sh/tq7mxd2kw9pl41a/BBR8NpXwQ3hLm6TzvKe2YUJ5b?dl=0

Target Market(s)

People (or friends & family) suffering with the shame of mental health struggles

Industry/Entity Type

Mental Health

Font styles to use
Other font styles liked:
• Avenir

Colors
3276b5
85acd3
cfdeed

Requirements
Must have
• Relatable, contemporary, authentic & compelling
• Link for photos
• https://www.filqorvex.com/sh/tq7mxd2kw9pl41a/BBR8NpXwQ3hLm6TzvKe2YUJ5b?dl=0
Nice to have
• Abstract & creative
Should not have
• Cheesy, plastic, pedestrian etc

```html
<!DOCTYPE html>
<html lang="en">
<head>
<meta charset="utf-8">
<title>Glow Beyond It – Book Cover</title>
<link rel="stylesheet" href="https://fonts.googleapis.com/css2?family=Nunito+Sans:wght@400;700&display=swap">
<style>
  :root {
    --page-bg: #ffffff;
    --cover-black: #03050c;
    --cover-navy: #0a1640;
    --glow-blue: #3276b5;
    --glow-mid: #85acd3;
    --glow-pale: #cfdeed;
    --title-white: #ffffff;
  }
  html, body {
    margin: 0;
    padding: 0;
    width: 1200px;
    height: 900px;
    overflow: hidden;
    background: var(--page-bg);
  }
  .canvas {
    position: relative;
    width: 1200px;
    height: 900px;
    background: var(--page-bg);
  }
  .book-cover {
    position: absolute;
    left: 282px;
    top: 0;
    width: 636px;
    height: 900px;
    overflow: hidden;
    background: var(--cover-black);
    font-family: "Nunito Sans", "Avenir", sans-serif;
  }
  .cover-portrait {
    position: absolute;
    inset: 0;
    background:
      radial-gradient(ellipse 38% 30% at 50% 32%, rgba(133,172,211,0.55), rgba(50,118,181,0.35) 55%, transparent 100%),
      radial-gradient(ellipse 55% 45% at 58% 62%, rgba(50,118,181,0.55), rgba(10,22,64,0.6) 60%, transparent 100%),
      radial-gradient(circle at 92% 18%, rgba(133,172,211,0.5), transparent 9%),
      radial-gradient(circle at 76% 7%, rgba(50,118,181,0.35), transparent 10%),
      linear-gradient(180deg, var(--cover-black) 0%, var(--cover-navy) 55%, var(--cover-black) 100%);
  }
  .brand-mark {
    position: absolute;
    left: 36px;
    top: 34px;
    display: flex;
    align-items: center;
    gap: 10px;
  }
  .brand-square {
    width: 16px;
    height: 16px;
    background: var(--glow-blue);
  }
  .brand-name {
    font-size: 22px;
    font-weight: 400;
    color: var(--glow-mid);
    letter-spacing: 0.5px;
  }
  .cover-title {
    position: absolute;
    left: 18px;
    right: 18px;
    top: 560px;
    margin: 0;
    color: var(--title-white);
    font-weight: 400;
    font-size: 106px;
    line-height: 0.9;
    letter-spacing: 1px;
    text-transform: uppercase;
  }
  .cover-title .title-line { display: block; }
  .cover-subtitle {
    position: absolute;
    left: 22px;
    right: 18px;
    top: 823px;
    margin: 0;
    color: var(--title-white);
    font-weight: 700;
    font-size: 26.5px;
    letter-spacing: 0.6px;
    text-transform: uppercase;
    white-space: nowrap;
  }
</style>
</head>
<body>
  <div class="canvas">
    <section class="book-cover">
      <div class="cover-portrait" role="img" aria-label="Blue-lit portrait photograph of the author seated against a dark background"></div>
      <div class="brand-mark">
        <span class="brand-square"></span>
        <span class="brand-name">ned calloway</span>
      </div>
      <h1 class="cover-title">
        <span class="title-line">Glow</span>
        <span class="title-line">Beyond It</span>
      </h1>
      <p class="cover-subtitle">Rewriting quiet inner battles</p>
    </section>
  </div>
</body>
</html>
```